KFT Hearth Journal

Create a 1 page ad for advertising magazine. link is below and examples of our competitors are on pages 14, 45, 53, 57, 87, 76. page 61 is our current ad.

we are a multifamily general contractor specializing in interior and exterior renovations. our website for info is bellwoodbuild.example

http://pagerack.example/kft_hearth/docs/hearth_may2018

```html
<!DOCTYPE html>
<html lang="en">
<head>
<meta charset="utf-8">
<title>Bellwood Build – Multifamily General Contractor Ad</title>
<link href="https://fonts.googleapis.com/css2?family=Roboto+Condensed:wght@400;700&family=Questrial&family=Roboto:wght@100;400&display=swap" rel="stylesheet">
<style>
  :root{
    --navy:#12436f;
    --sky:#b3c8e8;
    --ink:#1c1f26;
    --white:#ffffff;
    --page:#eef0f3;
    --photo-interior:linear-gradient(160deg,#6b5a4a 0%,#3b2a20 55%,#2a1c14 100%);
    --photo-exterior:linear-gradient(170deg,#8fb0d8 0%,#c9b15a 45%,#7e8a52 100%);
  }
  *{box-sizing:border-box;margin:0;padding:0}
  html,body{width:680px;height:1200px;overflow:hidden;background:var(--page)}
  .ad{
    position:absolute;left:40px;top:212px;width:600px;height:776px;
    background:var(--white);box-shadow:0 6px 18px rgba(0,0,0,.25);
    display:grid;grid-template-columns:300px 300px;grid-template-rows:375px 230px 104px 67px;
  }
  .headline{
    background:var(--navy);color:var(--white);
    font-family:"Roboto Condensed",sans-serif;font-weight:700;font-size:34px;
    text-align:right;padding:72px 28px 0 0;line-height:51px;
  }
  .services{
    background:var(--sky);color:var(--ink);
    font-family:"Questrial",sans-serif;padding:80px 0 0 28px;
  }
  .services span{display:block}
  .services .small{font-size:27px;line-height:38px}
  .services .large{font-size:41px;line-height:44px}
  .photo{position:relative;overflow:hidden}
  .photo-interior{background:var(--photo-interior)}
  .photo-exterior{background:var(--photo-exterior)}
  .photo-label{
    position:absolute;left:0;right:0;height:50px;
    background:rgba(80,100,140,.45);color:rgba(255,255,255,.85);
    font-family:"Roboto",sans-serif;font-weight:100;font-size:40px;letter-spacing:1px;
    display:flex;align-items:center;
  }
  .photo-interior .photo-label{top:93px;justify-content:flex-end;padding-right:12px}
  .photo-exterior .photo-label{top:142px;padding-left:10px;right:90px}
  .brand{
    grid-column:1 / 3;display:flex;align-items:center;justify-content:center;gap:14px;
    box-shadow:0 10px 10px -8px rgba(0,0,0,.5);position:relative;z-index:1;
  }
  .brand-mark{width:46px;height:46px;background:var(--navy)}
  .brand-name{
    font-family:"Roboto Condensed",sans-serif;font-weight:700;font-size:38px;color:var(--navy);line-height:1;
  }
  .brand-name small{display:block;font-size:13px;letter-spacing:3px;margin-top:4px}
  .contacts{
    background:var(--navy);color:var(--white);
    font-family:"Roboto Condensed",sans-serif;font-size:11.5px;line-height:15px;
    text-align:right;padding:20px 12px 0 0;
  }
  .website{
    background:var(--sky);color:var(--navy);
    font-family:"Roboto Condensed",sans-serif;font-size:19px;
    display:flex;align-items:center;padding-left:12px;
  }
</style>
</head>
<body>
<main class="ad">
  <h1 class="headline">WE<br>ARE A<br>MULTIFAMILY<br>GENERAL<br>CONTRACTOR</h1>
  <p class="services">
    <span class="small">SPECIALIZING</span>
    <span class="small">IN</span>
    <span class="large">INTERIOR</span>
    <span class="small">AND</span>
    <span class="large">EXTERIOR</span>
    <span class="small">RENOVATIONS.</span>
  </p>
  <div class="photo photo-interior" role="img" aria-label="Renovated interior hall with wood floors and arched windows">
    <span class="photo-label">INTERIOR</span>
  </div>
  <div class="photo photo-exterior" role="img" aria-label="Renovated yellow wooden house exterior with grey roof">
    <span class="photo-label">EXTERIOR</span>
  </div>
  <div class="brand">
    <span class="brand-mark"></span>
    <span class="brand-name">BELLWOOD BUILD<small>GENERAL CONTRACTORS</small></span>
  </div>
  <p class="contacts">DALLAS: 877-555-0142 / 214-555-0187<br>AUSTIN: 512-555-0163 HOUSTON: 832-555-0129</p>
  <p class="website">WWW//BELLWOODBUILD.EXAMPLE</p>
</main>
</body>
</html>
```